New Flyer Design Project

I would like to purchase a customized version of a design you have previously submitted - https://www.plorvania.com/design/58204719

I want this to be something that looks really good.
We use this to explain our service agreements.
our website is www.bqumesh.net I want to stick with those colors.

```html
<!DOCTYPE html>
<html lang="en">
<head>
<meta charset="utf-8">
<title>Bqumesh Support Plans</title>
<link rel="stylesheet" href="https://fonts.googleapis.com/css2?family=Poppins:wght@400;500;700;800&display=swap">
<style>
  :root {
    --red: #d0262c;
    --red-deep: #9a2226;
    --red-dark: #7f1c20;
    --grey-band: #6b6b70;
    --text: #5a5a5e;
    --line: #d9d9dc;
    --paper: #ffffff;
    --tick-ring: #9a9a9e;
  }
  * { box-sizing: border-box; margin: 0; padding: 0; }
  html, body { width: 1200px; height: 829px; overflow: hidden; background: var(--paper); }
  body { position: relative; font-family: "Poppins", sans-serif; color: var(--text); }

  .header-shape { position: absolute; left: 0; top: 0; width: 1200px; height: 240px; }

  .title {
    position: absolute; left: 154px; top: 50px;
    font-weight: 800; font-size: 46px; letter-spacing: 0.3px;
    color: var(--paper); line-height: 1; white-space: nowrap;
  }

  .brand {
    position: absolute; left: 836px; top: 70px;
    color: var(--paper); font-weight: 700;
  }
  .brand-name { display: flex; align-items: center; gap: 8px; font-size: 30px; line-height: 1; letter-spacing: 1px; }
  .brand-mark { width: 12px; height: 12px; border-radius: 50%; background: var(--paper); }
  .brand-tag { font-weight: 400; font-size: 11.5px; margin-top: 9px; letter-spacing: 0.1px; white-space: nowrap; }

  .plans {
    position: absolute; left: 159px; top: 149px; width: 904px; height: 621px;
    border: 1px solid var(--line); border-top: none;
    border-radius: 16px 16px 34px 16px;
    background: rgba(255,255,255,0.9);
  }
  .plans-head {
    display: grid; grid-template-columns: 468px 217px 1fr;
    height: 82px; border-radius: 14px 14px 0 0;
    background: linear-gradient(90deg, var(--red-dark) 0%, var(--red-deep) 40%, var(--red) 100%);
    color: var(--paper);
  }
  .plans-head > div { display: flex; align-items: center; }
  .plans-head > div + div { border-left: 1px solid rgba(255,255,255,0.85); }
  .col-services { padding-left: 42px; font-weight: 700; font-size: 24px; }
  .plan { padding-left: 30px; font-weight: 800; font-size: 24px; line-height: 1.05; }
  .plan-text { display: block; white-space: nowrap; }
  .plan-text span { display: block; }
  .plan small { font-size: 14px; font-weight: 800; }

  .plans-body {
    position: absolute; left: 0; top: 82px; right: 0; bottom: 0;
    display: grid; grid-template-columns: 468px 217px 1fr;
  }
  .plans-body > .divider-col + .divider-col { border-left: 1px solid var(--line); }
  .rows { position: absolute; left: 0; right: 0; top: 10px; }
  .row { display: grid; grid-template-columns: 468px 217px 1fr; height: 28.3px; align-items: center; }
  .service { padding-left: 69px; font-size: 13.6px; font-weight: 500; color: var(--text); white-space: nowrap; }
  .cell { display: flex; justify-content: center; align-items: center; }
  .cell svg { width: 16px; height: 16px; }
  .available { color: var(--red); font-size: 13.6px; font-weight: 500; }

  .security-art {
    position: absolute; left: 47px; top: 651px; width: 198px; height: 137px;
    border-radius: 22px 22px 10px 10px;
    background: radial-gradient(ellipse at 40% 45%, #8a8a90 0%, #b9b9bd 55%, rgba(255,255,255,0) 78%),
                linear-gradient(90deg, rgba(208,38,44,0.35), rgba(208,38,44,0) 40%);
  }
</style>
</head>
<body>
  <svg class="header-shape" viewBox="0 0 1200 240" aria-hidden="true">
    <defs>
      <linearGradient id="headerRed" x1="0" x2="1" y1="0" y2="0">
        <stop offset="0" stop-color="#c1232a"/>
        <stop offset="1" stop-color="#9a2226"/>
      </linearGradient>
    </defs>
    <path d="M0,0 H1200 V88 Q600,200 0,80 Z" fill="url(#headerRed)"/>
    <path d="M0,93 Q80,135 168,160 Q80,140 0,126 Z" fill="var(--grey-band)"/>
  </svg>

  <h1 class="title">BQUMESH SUPPORT PLANS</h1>

  <div class="brand">
    <div class="brand-name"><span>BQUMESH</span><span class="brand-mark"></span></div>
    <div class="brand-tag">managed network services</div>
  </div>

  <div class="security-art" role="img" aria-label="Padlock with shield, cloud and password field illustration"></div>

  <svg width="0" height="0" style="position:absolute" aria-hidden="true">
    <symbol id="tick" viewBox="0 0 16 16">
      <circle cx="8" cy="8" r="7" fill="none" stroke="var(--tick-ring)" stroke-width="1"/>
      <path d="M4.6,8.2 L7,10.6 L11.6,5.2" fill="none" stroke="var(--red)" stroke-width="1.8" stroke-linecap="round" stroke-linejoin="round"/>
    </symbol>
  </svg>

  <section class="plans">
    <div class="plans-head">
      <div class="col-services">Services</div>
      <div class="plan"><span class="plan-text"><span>Security Plus</span><span>$75.00</span></span></div>
      <div class="plan"><span class="plan-text"><span>IT Essentials</span><span>$55.00 <small>Per PC</small></span></span></div>
    </div>
    <div class="plans-body">
      <div class="divider-col"></div><div class="divider-col"></div><div class="divider-col"></div>
      <div class="rows">
        <div class="row"><span class="service">Unlimited US bases Remote Help Desk Support</span><span class="cell"><svg><use href="#tick"/></svg></span><span class="cell"><svg><use href="#tick"/></svg></span></div>
        <div class="row"><span class="service">Unlimited On-Site Support</span><span class="cell"><svg><use href="#tick"/></svg></span><span class="cell available">Available</span></div>
        <div class="row"><span class="service">Advanced Cybersecurity and Threat Hunting</span><span class="cell"><svg><use href="#tick"/></svg></span><span class="cell available">Available</span></div>
        <div class="row"><span class="service">Managed Antivirus Protection</span><span class="cell"><svg><use href="#tick"/></svg></span><span class="cell"><svg><use href="#tick"/></svg></span></div>
        <div class="row"><span class="service">Multifactor Authentication Powered by Vaultkey</span><span class="cell"><svg><use href="#tick"/></svg></span><span class="cell available">Available</span></div>
        <div class="row"><span class="service">Cyber Security Awareness Training</span><span class="cell"><svg><use href="#tick"/></svg></span><span class="cell available">Available</span></div>
        <div class="row"><span class="service">Enhanced Span Filtering</span><span class="cell"><svg><use href="#tick"/></svg></span><span class="cell available">Available</span></div>
        <div class="row"><span class="service">Internet Content Filtering</span><span class="cell"><svg><use href="#tick"/></svg></span><span class="cell available">Available</span></div>
        <div class="row"><span class="service">Proactive Security and System Monitoring</span><span class="cell"><svg><use href="#tick"/></svg></span><span class="cell"><svg><use href="#tick"/></svg></span></div>
        <div class="row"><span class="service">Security and Vulnerability patching</span><span class="cell"><svg><use href="#tick"/></svg></span><span class="cell"><svg><use href="#tick"/></svg></span></div>
        <div class="row"><span class="service">Backup and disaster recovery</span><span class="cell"><svg><use href="#tick"/></svg></span><span class="cell"><svg><use href="#tick"/></svg></span></div>
        <div class="row"><span class="service">Network Management and Administration</span><span class="cell"><svg><use href="#tick"/></svg></span><span class="cell"><svg><use href="#tick"/></svg></span></div>
        <div class="row"><span class="service">Lumora Office Suite Administration and Configuration</span><span class="cell"><svg><use href="#tick"/></svg></span><span class="cell"><svg><use href="#tick"/></svg></span></div>
        <div class="row"><span class="service">Lumora Cloud Administration and Configuration</span><span class="cell"><svg><use href="#tick"/></svg></span><span class="cell"><svg><use href="#tick"/></svg></span></div>
        <div class="row"><span class="service">Lumora Desktop and Server Support</span><span class="cell"><svg><use href="#tick"/></svg></span><span class="cell"><svg><use href="#tick"/></svg></span></div>
        <div class="row"><span class="service">Managed DNS</span><span class="cell"><svg><use href="#tick"/></svg></span><span class="cell"><svg><use href="#tick"/></svg></span></div>
        <div class="row"><span class="service">Hardware and Software Procurement</span><span class="cell"><svg><use href="#tick"/></svg></span><span class="cell"><svg><use href="#tick"/></svg></span></div>
        <div class="row"><span class="service">Assett Management</span><span class="cell"><svg><use href="#tick"/></svg></span><span class="cell"><svg><use href="#tick"/></svg></span></div>
      </div>
    </div>
  </section>
</body>
</html>
```